Business card for start up company

SIMPLE, CLEAN, FRESH, MODERN, SOPHISTICATED. professional. experienced, easy to deal with, expert in the field. local ethics.

professional business card for Forge Ahead Works. using company logo supplied and images.

GENERAL ENGINEERING - MACHINING - WELDING - MAINTENANCE

Forge Ahead Works Ltd is a locally owned mechanical engineering company that specialises in general and mechanical engineering, as well as steel fabrication, welding, repairs and maintenance.

We specialise in the design, welding, fabrication and installation of stainless and mild steel fabrications. We service commercial and residential clients; large or small projects; production line or one off designs.

We have built a solid reputation for quality and service for our machinery and engineering work around Northland NZ. For innovative, cost effective and efficient engineering solutions, to suit a wide range of commercial, residential and rural applications.

Target Market(s)

boat builders. DIY. industrial. RESIDENTIAL. COMMERCIAL

Industry/Entity Type

Mechanical Engineering

Contact Information for Business Card

CONTACT / SERVICES SIDE
Forge Ahead Works Ltd.
Design | Machining | Welding | Fabrication | Installation | Maintenance
www.forgeaheadworks.example.nz
grant@forgeaheadworks.example.nz

Font styles to use
Serif

Colors

Designer to choose colors to be used in the design.

Requirements
Must have
• LOGO ONLY WITH NEGATIVE SPACE ON FRONT SIDE
• services and contact side , either use stock photos (supplied) as background or background supplied in logo photos.
Nice to have
• use the symbol icon in logo on contact/ services side, , enlarged, transparent and faded into the background with text over the top on the
• Design | Machining | Welding | Fabrication | Installation | Maintenance
• the above services to be subtle, along the bottom edge of the services side. can i also have another proof with eh above services featuring on the bottom edge of the LOGO FRONT side to see if the text looks better with or without.
Should not have
• crowded, busy, different fonts. different casing.
• use fonts in the logo files designer to make font decision.

```html
<!DOCTYPE html>
<html lang="en">
<head>
<meta charset="utf-8">
<title>Forge Ahead Works – Business Card</title>
<link rel="stylesheet" href="https://fonts.googleapis.com/css2?family=Montserrat:wght@400;700&family=Tinos:wght@400;700&display=swap">
<style>
  :root {
    --canvas: #2e2e2e;
    --card-dark: #151515;
    --card-dark-soft: #3a3a3a;
    --paper: #ffffff;
    --ink: #3a3a3c;
    --ink-soft: #4a4a4c;
    --accent: #e8541f;
    --band: #434345;
    --light-text: #e6e6e6;
  }
  * { margin: 0; padding: 0; box-sizing: border-box; }
  html, body { width: 1200px; height: 880px; overflow: hidden; }
  body {
    background: var(--canvas);
    font-family: "Tinos", "Times New Roman", serif;
    position: relative;
  }
  .card {
    position: absolute;
    left: 250px;
    width: 700px;
    height: 400px;
    overflow: hidden;
    box-shadow: 0 10px 30px rgba(0,0,0,.45);
  }

  /* Front: logo side */
  .card--front { top: 30px; background: var(--card-dark); }
  .front-backdrop {
    position: absolute; inset: 0;
    background:
      linear-gradient(118deg, transparent 40%, rgba(255,255,255,.14) 52%, rgba(255,255,255,.05) 58%, transparent 66%),
      linear-gradient(160deg, var(--card-dark-soft) 0%, var(--card-dark) 45%, #0c0c0c 100%);
  }
  .front-brand {
    position: absolute; left: 0; right: 0; top: 150px;
    display: flex; align-items: center; justify-content: center; gap: 18px;
  }
  .front-brand__mark { width: 26px; height: 26px; background: var(--accent); }
  .front-brand__name {
    color: var(--light-text); font-size: 44px; font-weight: 400; letter-spacing: 2px;
    text-transform: uppercase;
  }
  .front-services {
    position: absolute; left: 0; right: 0; bottom: 70px;
    text-align: center; color: var(--light-text); font-size: 17px; letter-spacing: .5px;
  }

  /* Back: contact side */
  .card--back { top: 450px; background: var(--paper); }
  .back-brand {
    position: absolute; left: 40px; top: 120px; width: 240px;
    display: flex; flex-direction: column; align-items: flex-start; gap: 14px;
  }
  .back-brand__mark { width: 30px; height: 30px; background: var(--accent); margin-left: 150px; }
  .back-brand__name {
    color: var(--ink); font-size: 40px; line-height: 1.05; font-weight: 700; text-transform: uppercase;
  }
  .back-divider {
    position: absolute; left: 300px; top: 100px; width: 1px; height: 150px; background: var(--accent);
  }
  .contact { position: absolute; left: 330px; top: 70px; color: var(--ink); }
  .contact__company {
    font-family: "Montserrat", Arial, sans-serif; font-size: 24px; font-weight: 400;
    text-transform: uppercase; letter-spacing: .5px; margin-bottom: 14px; white-space: nowrap;
  }
  .contact__person { font-size: 26px; font-weight: 700; line-height: 1; }
  .contact__role { font-size: 18px; color: var(--accent); margin-bottom: 22px; }
  .contact__line { display: flex; align-items: center; gap: 10px; font-size: 16px; margin-bottom: 6px; }
  .contact__icon { width: 20px; height: 20px; flex: none; }
  .corner-mark {
    position: absolute; right: 0; top: 0; width: 36px; height: 36px; background: var(--accent);
  }
  .services-band {
    position: absolute; left: 0; right: 0; bottom: 22px; height: 36px;
    background: var(--band); color: #fff; font-size: 17px;
    display: flex; align-items: center; justify-content: center; letter-spacing: .5px;
  }
</style>
</head>
<body>
  <section class="card card--front">
    <div class="front-backdrop" role="img" aria-label="Dark curved brushed steel sheet photograph"></div>
    <div class="front-brand">
      <span class="front-brand__mark"></span>
      <span class="front-brand__name">Forge Ahead Works</span>
    </div>
    <p class="front-services">Design | Machining | Welding | Fabrication | Installation | Maintenance</p>
  </section>

  <section class="card card--back">
    <span class="corner-mark"></span>
    <div class="back-brand">
      <span class="back-brand__mark"></span>
      <span class="back-brand__name">Forge Ahead Works</span>
    </div>
    <div class="back-divider"></div>
    <div class="contact">
      <p class="contact__company">Forge Ahead Works Ltd.</p>
      <p class="contact__person">Reid Talbot</p>
      <p class="contact__role">Manager</p>
      <p class="contact__line">
        <svg class="contact__icon" viewBox="0 0 20 20" aria-hidden="true">
          <circle cx="10" cy="10" r="10" fill="#e8541f"/>
          <circle cx="10" cy="10" r="5.5" fill="none" stroke="#fff" stroke-width="1.2"/>
          <ellipse cx="10" cy="10" rx="2.4" ry="5.5" fill="none" stroke="#fff" stroke-width="1"/>
          <line x1="4.5" y1="10" x2="15.5" y2="10" stroke="#fff" stroke-width="1"/>
        </svg>
        www.forgeaheadworks.example.nz
      </p>
      <p class="contact__line">
        <svg class="contact__icon" viewBox="0 0 20 20" aria-hidden="true">
          <circle cx="10" cy="10" r="10" fill="#e8541f"/>
          <rect x="5" y="6.5" width="10" height="7" fill="none" stroke="#fff" stroke-width="1.2"/>
          <polyline points="5,6.5 10,10.5 15,6.5" fill="none" stroke="#fff" stroke-width="1.2"/>
        </svg>
        grant@forgeaheadworks.example.nz
      </p>
    </div>
    <div class="services-band">Design | Machining | Welding | Fabrication | Installation | Maintenance</div>
  </section>
</body>
</html>
```